Wholesale in Gold Jewellery & Gold Bullion

We are an established gold jewellery and gold bullion wholesaler selling these products to international clients. We already have a name and logo of our company, hence please view attached current card design. We need a completely new design to compliment our business and industry and the final design should be new and elegant.

Contact Information for Business Card

New card details must be same as per current card. Like logo, name, tel no. & etc.

Colors

Designer to choose colors to be used in the design.

```html
<!DOCTYPE html>
<html lang="en">
<head>
<meta charset="utf-8">
<title>Aurelian &amp; Co – Business Card</title>
<link rel="stylesheet" href="https://fonts.googleapis.com/css2?family=Tinos:wght@400&family=Nunito:wght@600;700&display=swap">
<style>
  :root {
    --gold: #d8961c;
    --paper: #eceeed;
    --stage: #e9eaea;
    --ink: #151515;
    --white: #ffffff;
  }
  * { box-sizing: border-box; margin: 0; padding: 0; }
  html, body {
    width: 1200px; height: 1200px; overflow: hidden;
    background: var(--stage);
  }
  .sheet { position: relative; width: 1200px; height: 1200px; }
  .card {
    position: absolute; left: 180px; width: 840px; height: 480px;
    overflow: hidden;
    box-shadow: 0 2px 6px rgba(0,0,0,0.12);
  }

  /* Reverse side */
  .card--reverse { top: 90px; background: var(--gold); }
  .reverse__name {
    position: absolute; left: 0; right: 0; top: 218px;
    text-align: center;
    font-family: "Tinos", serif; font-size: 36px; letter-spacing: 1px;
    color: var(--white);
  }

  /* Front side */
  .card--front { top: 630px; background: var(--paper); }
  .front__band {
    position: absolute; left: 0; right: 0; bottom: 0; height: 96px;
    background: var(--gold);
  }
  .front__brand {
    position: absolute; left: 30px; top: 0; width: 350px; height: 384px;
    display: flex; align-items: center; justify-content: center;
  }
  .brand__name {
    font-family: "Tinos", serif; font-size: 21px; color: var(--ink);
    letter-spacing: 0.5px; white-space: nowrap;
  }
  .front__divider {
    position: absolute; left: 405px; top: 44px; width: 2px; height: 236px;
    background: var(--ink);
  }
  .front__details {
    position: absolute; left: 440px; top: 34px;
    font-family: "Nunito", sans-serif; color: var(--ink);
  }
  .person__name {
    font-weight: 700; font-size: 27px; color: var(--gold); line-height: 1.1;
  }
  .person__role { font-weight: 600; font-size: 19px; margin-bottom: 20px; }
  .address { font-weight: 600; font-size: 19px; line-height: 1.4; margin-bottom: 16px; }
  .contact-list { list-style: none; }
  .contact-list li {
    display: flex; align-items: center; gap: 12px;
    font-size: 17px; font-weight: 600; line-height: 1.55;
  }
  .contact-list svg { width: 18px; height: 18px; flex: none; }
</style>
</head>
<body>
<main class="sheet">
  <section class="card card--reverse" aria-label="Card reverse">
    <p class="reverse__name">AURELIAN &amp; CO PTE LTD</p>
  </section>

  <section class="card card--front" aria-label="Card front">
    <div class="front__brand">
      <p class="brand__name">AURELIAN &amp; CO PTE LTD</p>
    </div>
    <div class="front__divider"></div>
    <div class="front__details">
      <p class="person__name">Ravin Kesarwal</p>
      <p class="person__role">Director</p>
      <p class="address">18 Carrow Lane,<br>Singapore 208113.</p>
      <ul class="contact-list">
        <li>
          <svg viewBox="0 0 18 18" aria-hidden="true"><rect x="5" y="1.5" width="8" height="15" rx="1.5" fill="none" stroke="#151515" stroke-width="1.4"/><line x1="8" y1="14" x2="10" y2="14" stroke="#151515" stroke-width="1.4"/></svg>
          +65 6100 2400
        </li>
        <li>
          <svg viewBox="0 0 18 18" aria-hidden="true"><path d="M4 2 L7 2 L8 6 L6 7.5 Q7.5 11 10.5 12 L12 10 L16 11 L16 14 Q16 16 14 16 Q4 15 2 4 Q2 2 4 2 Z" fill="#151515"/></svg>
          +65 6100 2411
        </li>
        <li>
          <svg viewBox="0 0 18 18" aria-hidden="true"><rect x="2" y="8" width="14" height="8" rx="1.5" fill="none" stroke="#151515" stroke-width="1.4"/><path d="M2 7 Q9 1 16 7" fill="none" stroke="#151515" stroke-width="1.6"/><circle cx="9" cy="12" r="2" fill="#151515"/></svg>
          +65 9100 5522
        </li>
        <li>
          <svg viewBox="0 0 18 18" aria-hidden="true"><rect x="1.5" y="3.5" width="15" height="11" rx="1" fill="#151515"/><path d="M2.5 5 L9 10 L15.5 5" fill="none" stroke="#ffffff" stroke-width="1.4"/></svg>
          ravin@aurelianco.com
        </li>
      </ul>
    </div>
    <div class="front__band"></div>
  </section>
</main>
</body>
</html>
```